Velmira website

A clean uncluttered design that shows at glance that we are in the Media and design and publishing business.

We would like to see designs that use colours that show warmth and quality.

The website should show:
- products
- projects

These should be displaxed in spaces that we can add or interchanges with new products or projects.

Target Market(s)

Business and project managers and buyers and authors.

Industry/Entity Type

Business

Requirements
Must have
• Good colours. Not too strong, not weak, but reflecting quality.

```html
<!DOCTYPE html>
<html lang="en">
<head>
<meta charset="utf-8">
<title>Velmira</title>
<link href="https://fonts.googleapis.com/css2?family=Open+Sans:ital,wght@0,400;0,600;0,700;1,400&display=swap" rel="stylesheet">
<style>
:root{
  --brand-blue:#17509a;
  --nav-top:#1f5fab;
  --nav-bottom:#0e3c78;
  --nav-active:#2b2b2b;
  --link-blue:#0f4f9c;
  --text:#333;
  --muted:#666;
  --line:#dedede;
  --panel:#f6f6f6;
  --footer:#333333;
  --footer-base:#2a2a2a;
  --footer-green:#8cc63f;
  --btn-green:#5d9c1e;
}
*{box-sizing:border-box;margin:0;padding:0}
html,body{width:814px;height:1200px;overflow:hidden;background:#fff}
body{font-family:"Open Sans",Arial,sans-serif;color:var(--text)}
.page{position:relative;width:814px;height:1200px;overflow:hidden}
.abs{position:absolute}

.logo{left:68px;top:14px;font-size:34px;font-weight:700;color:var(--brand-blue);letter-spacing:.5px}
.search{left:610px;top:23px;width:137px;height:25px;border:1px solid #ccc;font-size:9px;color:#999;padding:6px 9px}
.search svg{position:absolute;right:6px;top:6px}

.main-nav{left:0;top:71px;width:814px;height:34px;background:linear-gradient(var(--nav-top),var(--nav-bottom))}
.main-nav a{position:absolute;top:0;height:34px;line-height:34px;color:#fff;font-size:10.5px;font-weight:600;text-decoration:none;text-transform:uppercase}
.main-nav a.active{background:var(--nav-active);padding:0 11px;left:67px}

.slider{left:67px;top:115px;width:680px;height:274px;border:3px solid #ddd;background:#05080b}
.slide-art{position:absolute;left:300px;top:0;width:374px;height:268px;background:radial-gradient(ellipse at 62% 45%,#bfe3ea 0%,#4f8a98 22%,#163440 50%,#05080b 80%)}
.slide-title{left:24px;top:57px;color:#f2f2f2;font-size:17px;font-weight:700;letter-spacing:.3px}
.slide-text{left:24px;top:86px;width:262px;color:#eee;font-size:9px;line-height:15.7px}
.slide-btn{left:24px;top:157px;width:85px;height:25px;background:#f5f5f5;border-radius:2px;font-size:11px;font-weight:700;color:#333;text-align:center;line-height:25px}
.dots{left:26px;top:241px}
.dots span{display:inline-block;width:9px;height:9px;border-radius:50%;background:#ccc;margin-right:6px}
.dots span:first-child{background:#555;border:1px solid #999}

.feature{top:405px;width:156px;height:57px;border:1px solid #dcdcdc;background:linear-gradient(#fff,#f3f3f3)}
.feature svg{position:absolute;left:18px;top:10px}
.feature p{position:absolute;left:78px;top:10px;font-size:12.5px;font-weight:600;color:#555;line-height:17px;text-transform:uppercase}

.divider{left:68px;top:479px;width:679px;height:1px;background:var(--line)}
.section-title{left:68px;top:495px;font-size:12.5px;font-weight:700;color:var(--brand-blue)}

.project{top:527px;width:156px;height:226px;border:1px solid #ddd;background:linear-gradient(#fff,#f6f6f6)}
.project .thumb{position:absolute;left:5px;top:5px;width:146px;height:93px;border-radius:2px}
.project h3{position:absolute;left:7px;top:108px;width:145px;font-size:9px;font-weight:400;color:var(--link-blue);line-height:13.5px}
.project p{position:absolute;left:7px;top:139px;width:145px;font-size:8px;color:var(--muted);line-height:11.4px}
.project .more{position:absolute;left:8px;top:197px;height:18px;padding:0 6px;border:1px solid #ccc;background:#fff;font-size:7.5px;color:#555;line-height:16px}

.pager{left:542px;top:772px}
.pager span{display:inline-block;width:14px;height:14px;border:1px solid #ccc;background:#fff;margin-right:1px;position:relative}
.pager svg{position:absolute;left:3px;top:3px}

.quote{left:68px;top:808px;width:505px;height:90px;border:1px solid #e4e4e4;background:#f8f8f8;text-align:center}
.quote p{margin:15px 18px 0;font-size:12px;font-style:italic;color:#555;line-height:18.5px}
.quote cite{display:block;margin-top:7px;font-style:normal;font-size:11px;color:var(--link-blue)}

.side-panel{left:590px;width:156px;background:var(--panel)}
.side-panel h2{height:28px;background:linear-gradient(var(--nav-top),var(--nav-bottom));color:#fff;font-size:12.5px;font-weight:700;padding:5px 9px;text-transform:uppercase}
.side-item{position:relative;padding:14px 4px 0 20px;font-size:9px;line-height:14.2px}
.side-item a{color:var(--link-blue);text-decoration:none}
.side-item time{display:block;color:#333;margin-top:3px}
.side-item svg{position:absolute;left:3px;top:17px}

.contact-band{left:0;top:922px;width:814px;height:66px;background:#f4f4f4}
.contact-band .info{position:absolute;top:20px;font-size:9px;color:#777;line-height:15.5px}
.contact-band svg{position:absolute}

.footer{left:0;top:988px;width:814px;height:171px;background:var(--footer)}
.footer h4{position:absolute;top:16px;font-size:12px;font-weight:400;color:var(--footer-green)}
.footer ul{position:absolute;top:45px;list-style:none}
.footer li{font-size:9px;color:#eee;line-height:17px}
.footer .note{position:absolute;left:440px;top:43px;width:175px;font-size:9px;color:#bbb;line-height:13px}
.footer .field{position:absolute;left:440px;width:166px;height:18px;background:#fff;border-radius:2px;font-size:8.5px;color:#666;padding:3px 9px}
.footer .subscribe{position:absolute;left:542px;top:124px;width:64px;height:19px;background:linear-gradient(#7ab83a,var(--btn-green));color:#fff;font-size:8.5px;text-align:center;line-height:19px;border-radius:2px}
.social{position:absolute;left:647px;font-size:9px;color:#eee;line-height:18px}
.social i{display:inline-block;width:18px;height:18px;border-radius:50%;background:#fff;vertical-align:middle;margin-right:9px}

.copyright{left:0;top:1159px;width:814px;height:41px;background:var(--footer-base);text-align:center;font-size:8.5px;color:#aaa;line-height:41px}
</style>
</head>
<body>
<div class="page">

<header>
  <div class="abs logo">VELMIRA</div>
  <div class="abs search">Search
    <svg width="12" height="12" viewBox="0 0 12 12"><circle cx="4.5" cy="4.5" r="3.3" fill="none" stroke="#333" stroke-width="1.8"/><line x1="7" y1="7" x2="11" y2="11" stroke="#333" stroke-width="2.4"/></svg>
  </div>
</header>

<nav class="abs main-nav">
  <a class="active" href="#">Home</a>
  <a href="#" style="left:143px">Who we are</a>
  <a href="#" style="left:240px">What we do</a>
  <a href="#" style="left:338px">Gallery</a>
  <a href="#" style="left:413px">Awards</a>
  <a href="#" style="left:488px">Advetise with us</a>
  <a href="#" style="left:610px">News</a>
  <a href="#" style="left:672px">Contact us</a>
</nav>

<section class="abs slider">
  <div class="slide-art" role="img" aria-label="Open book glowing with light rays against a starry dark sky"></div>
  <h1 class="abs slide-title">WELCOME TO VELMIRA</h1>
  <p class="abs slide-text">Nunc ullamcorper lectus mollis volutpat. Curabitur a mauris ac diam aliquam tristique. Praesent bibendum eget urna id mollis. Vestibulum id ligula erat. Donec libero purus, imperdiet at eleifend in, venenatis ut arcu.</p>
  <div class="abs slide-btn">CONTACT US</div>
  <div class="abs dots"><span></span><span></span><span></span><span></span></div>
</section>

<div class="abs feature" style="left:68px">
  <svg width="48" height="36" viewBox="0 0 48 36"><rect x="14" y="3" width="30" height="24" fill="none" stroke="#555" stroke-width="3"/><rect x="22" y="29" width="14" height="3" fill="#555"/><rect x="2" y="14" width="14" height="20" fill="#fff" stroke="#555" stroke-width="3"/><rect x="8" y="31" width="2" height="1" fill="#555"/></svg>
  <p>Media<br>Services</p>
</div>
<div class="abs feature" style="left:242px">
  <svg width="46" height="36" viewBox="0 0 46 36"><path d="M4 6 Q14 2 22 7 L22 34 Q14 29 4 33 Z" fill="#555"/><path d="M24 7 Q32 2 42 6 L42 33 Q32 29 24 34 Z" fill="#555"/></svg>
  <p>Book<br>Publishing</p>
</div>
<div class="abs feature" style="left:416px">
  <svg width="46" height="36" viewBox="0 0 46 36"><circle cx="23" cy="18" r="15" fill="none" stroke="#555" stroke-width="4"/><circle cx="23" cy="18" r="8" fill="none" stroke="#555" stroke-width="4"/><circle cx="23" cy="18" r="2.5" fill="#555"/></svg>
  <p>Advetise<br>With us</p>
</div>
<div class="abs feature" style="left:590px">
  <svg width="46" height="40" viewBox="0 0 46 40"><path d="M14 22 L10 38 L16 34 L19 38 L22 24 Z M32 22 L36 38 L30 34 L27 38 L24 24 Z" fill="#555"/><circle cx="23" cy="14" r="12" fill="#555"/><circle cx="23" cy="14" r="7" fill="#fff"/><circle cx="23" cy="14" r="4" fill="#555"/></svg>
  <p>Our<br>Awards</p>
</div>

<div class="abs divider"></div>

<main>
  <h2 class="abs section-title">OUR PROJECTS</h2>

  <article class="abs project" style="left:68px">
    <div class="thumb" role="img" aria-label="Student reading a book between library shelves" style="background:linear-gradient(135deg,#c9c2b4,#8a6e63 50%,#4f5f7a)"></div>
    <h3>Nunc ullamcorper lectus necma mollis volutpat.</h3>
    <p>Donec libero purus, imperdiet at eleifend in, venenatis ut arcu. Quisque convallis ligula mattis magna suscipit tincidunt.</p>
    <span class="more">READ MORE</span>
  </article>
  <article class="abs project" style="left:242px">
    <div class="thumb" role="img" aria-label="Studio microphone above a mixing desk" style="background:linear-gradient(135deg,#d8c49a,#9c8a6c 50%,#4b4a4a)"></div>
    <h3>Nunc ullamcorper lectus necma mollis volutpat.</h3>
    <p>Donec libero purus, imperdiet at eleifend in, venenatis ut arcu. Quisque convallis ligula mattis magna suscipit tincidunt.</p>
    <span class="more">READ MORE</span>
  </article>
  <article class="abs project" style="left:416px">
    <div class="thumb" role="img" aria-label="Concert crowd with raised hands under red stage lights" style="background:linear-gradient(#e8413a,#a8141a 55%,#2a0607)"></div>
    <h3>Nunc ullamcorper lectus necma mollis volutpat.</h3>
    <p>Donec libero purus, imperdiet at eleifend in, venenatis ut arcu. Quisque convallis ligula mattis magna suscipit tincidunt.</p>
    <span class="more">READ MORE</span>
  </article>

  <div class="abs pager">
    <span><svg width="8" height="8" viewBox="0 0 8 8"><path d="M5.5 1 L2.5 4 L5.5 7" fill="none" stroke="#555" stroke-width="1.2"/></svg></span><span><svg width="8" height="8" viewBox="0 0 8 8"><path d="M2.5 1 L5.5 4 L2.5 7" fill="none" stroke="#555" stroke-width="1.2"/></svg></span>
  </div>

  <blockquote class="abs quote">
    <p>&ldquo; Donec non elit a eros rhoncus lobortis. Ut arcu orci, malesuada ac luctus et, semper sit amet tellus. Integer a mauris in purus ultrices tincidunt. &rdquo;</p>
    <cite>Pellentesque venenatis</cite>
  </blockquote>
</main>

<aside>
  <div class="abs side-panel" style="top:497px;height:198px">
    <h2>Latest News</h2>
    <div class="side-item"><svg width="6" height="8" viewBox="0 0 6 8"><path d="M1 1 L4 4 L1 7" fill="none" stroke="#888"/></svg><a href="#">Donec magna ante, congue ut nunc nec, aliquam elementum augue quis leo.</a><time>January 2, 2014</time></div>
    <div class="side-item"><svg width="6" height="8" viewBox="0 0 6 8"><path d="M1 1 L4 4 L1 7" fill="none" stroke="#888"/></svg><a href="#">Donec magna ante, congue ut nunc nec, aliquam elementum augue quis leo.</a><time>January 2, 2014</time></div>
  </div>
  <div class="abs side-panel" style="top:708px;height:191px">
    <h2>Latest Events</h2>
    <div class="side-item"><svg width="6" height="8" viewBox="0 0 6 8"><path d="M1 1 L4 4 L1 7" fill="none" stroke="#888"/></svg><a href="#">Donec magna ante, congue ut nunc nec, aliquam elementum augue quis leo.</a><time>January 2, 2014</time></div>
    <div class="side-item"><svg width="6" height="8" viewBox="0 0 6 8"><path d="M1 1 L4 4 L1 7" fill="none" stroke="#888"/></svg><a href="#">Donec magna ante, congue ut nunc nec, aliquam elementum augue quis leo.</a><time>January 2, 2014</time></div>
  </div>
</aside>

<section class="abs contact-band">
  <svg style="left:80px;top:22px" width="16" height="20" viewBox="0 0 16 20"><rect x="1" y="1" width="14" height="18" fill="#999"/><rect x="5" y="5" width="6" height="14" fill="#f4f4f4"/></svg>
  <div class="info" style="left:105px;top:12px">55, Building name, streetname<br>City - Zip code</div>
  <svg style="left:263px;top:20px" width="20" height="22" viewBox="0 0 20 22"><path d="M3 2 L8 2 L9 7 L6 9 Q9 14 13 16 L15 13 L19 15 L19 20 Q8 20 2 8 Z" fill="#999"/></svg>
  <div class="info" style="left:290px">Phone: 555 014 2871</div>
  <svg style="left:434px;top:20px" width="20" height="20" viewBox="0 0 20 20"><rect x="1" y="7" width="18" height="12" fill="#999"/><rect x="5" y="1" width="10" height="7" fill="#fff" stroke="#999" stroke-width="1.5"/><rect x="4" y="10" width="12" height="2" fill="#f4f4f4"/><rect x="4" y="14" width="12" height="2" fill="#f4f4f4"/></svg>
  <div class="info" style="left:463px">Fax : 555 014 2872</div>
  <svg style="left:603px;top:24px" width="20" height="14" viewBox="0 0 20 14"><rect x="0" y="0" width="20" height="14" fill="#999"/><path d="M0 0 L10 8 L20 0" fill="none" stroke="#f4f4f4" stroke-width="1.5"/></svg>
  <div class="info" style="left:630px">E-mail : info@velmira.com</div>
</section>

<footer class="abs footer">
  <h4 style="left:79px">Quick Links</h4>
  <ul style="left:80px"><li>Home</li><li>Who we are</li><li>What we do</li><li>Gallery</li><li>Awards</li><li>Advetise with us</li><li>News</li></ul>
  <h4 style="left:197px">Support Links</h4>
  <ul style="left:199px"><li>Gallery</li><li>Testimonials</li><li>Jobs</li><li>Categories</li></ul>
  <h4 style="left:318px">Support Links</h4>
  <ul style="left:320px"><li>Contact us</li><li>Press</li><li>Legal Notice</li><li>Privacy Policy</li><li>Term of Use</li></ul>
  <h4 style="left:439px">Newsletters Sign Up</h4>
  <p class="note">Sign up for our daily email by entering your information below</p>
  <div class="field" style="top:76px">Your name</div>
  <div class="field" style="top:99px">Email address</div>
  <div class="subscribe">SUBSCRIBE</div>
  <h4 style="left:647px">Connect With Us</h4>
  <div class="social" style="top:47px"><i></i>Circlepage</div>
  <div class="social" style="top:70px"><i></i>Chirper</div>
  <div class="social" style="top:92px"><i></i>Proflink</div>
</footer>

<div class="abs copyright">Copyright &copy; 2014 &nbsp;VELMIRA. &nbsp;All rights reserved.</div>

</div>
</body>
</html>
```